plumbers buisness card

A buisness card for a plumbing buisness
needs to have a water theme with navy blue, light blue and white
with an image of either a water drop, pipes, tools or something relating to plumbing and incorperating my buisness name as a logo

"Kesterly Plumbing" is the words that need to stand out with "& gasfitting" to be smaller
Updates

spelling error on brief, "maintenance"
and also could you include my email m_kesterly@mailnest.com.au

Industry/Entity Type

Plumbing

Contact Information for Business Card

Kesterly Plumbing & Gasfitting

marcus kesterly
0493612085

specialising in
-new homes
-maitenance
-renovations

license no.
-73804

```html
<!DOCTYPE html>
<html lang="en">
<head>
<meta charset="UTF-8">
<title>Kesterly Plumbing &amp; Gasfitting – Business Card</title>
<link rel="stylesheet" href="https://fonts.googleapis.com/css2?family=Orbitron:wght@500;700&family=PT+Sans:wght@400;700&display=swap">
<style>
  :root {
    --backdrop: #d9dadc;
    --card-top: #1f55a4;
    --card-mid: #5f7fbf;
    --card-bottom: #eef1f8;
    --white: #ffffff;
    --accent: #f7941d;
    --ink: #1d1d1f;
    --ink-soft: #2b2b2e;
    --service: #6a3615;
    --rule: #3a2a20;
    --water-light: #c9e2f7;
    --water-mid: #7fb3e3;
  }
  * { box-sizing: border-box; margin: 0; padding: 0; }
  html, body { width: 1200px; height: 900px; overflow: hidden; }
  body {
    background: var(--backdrop);
    position: relative;
    font-family: "PT Sans", sans-serif;
  }
  .card {
    position: absolute;
    width: 615px;
    height: 338px;
    border-radius: 14px;
    background: linear-gradient(180deg, var(--card-top) 0%, var(--card-mid) 45%, var(--card-bottom) 100%);
    box-shadow: 0 4px 10px rgba(0,0,0,0.25);
    overflow: hidden;
  }
  .card--front { left: 83px; top: 72px; }
  .card--back { left: 483px; top: 492px; }

  .brand {
    position: absolute;
    right: 38px;
    top: 34px;
    text-align: right;
    color: var(--white);
    font-family: "Orbitron", sans-serif;
    line-height: 1;
    white-space: nowrap;
  }
  .card--back .brand { right: 88px; top: 36px; }
  .brand__name {
    display: flex;
    align-items: center;
    justify-content: flex-end;
    gap: 12px;
    font-size: 27px;
    font-weight: 700;
    letter-spacing: 0.5px;
  }
  .brand__mark {
    width: 16px;
    height: 16px;
    background: var(--accent);
    flex: none;
  }
  .brand__trade {
    display: block;
    font-size: 21px;
    font-weight: 500;
    margin-top: 8px;
  }

  .water-drop {
    position: absolute;
    left: 4px;
    top: 0;
    width: 140px;
    height: 328px;
    border-radius: 0 0 70px 70px;
    background: radial-gradient(ellipse at 50% 75%, var(--water-light) 0%, var(--water-mid) 45%, rgba(61,127,199,0) 75%);
  }

  .holder {
    position: absolute;
    right: 38px;
    top: 178px;
  }
  .holder__name {
    font-family: "Orbitron", sans-serif;
    font-weight: 700;
    font-size: 27px;
    line-height: 1;
    color: var(--ink);
    letter-spacing: 1px;
    text-transform: uppercase;
    white-space: nowrap;
  }
  .holder__licence {
    margin-top: 6px;
    font-size: 14px;
    font-weight: 700;
    color: var(--ink-soft);
  }

  .contact {
    position: absolute;
    right: 38px;
    top: 248px;
    text-align: right;
    color: var(--ink-soft);
  }
  .contact__email {
    font-size: 15px;
    font-weight: 700;
    line-height: 20px;
  }
  .contact__phone {
    margin-top: 6px;
    display: flex;
    justify-content: flex-end;
    align-items: center;
    gap: 6px;
    font-size: 18px;
    font-weight: 700;
    line-height: 22px;
  }
  .contact__phone svg { width: 14px; height: 20px; }

  .specialties {
    position: absolute;
    left: 0;
    right: 0;
    top: 125px;
    text-align: center;
  }
  .specialties__title {
    font-size: 17px;
    font-weight: 700;
    color: var(--white);
  }
  .specialties__list {
    list-style: none;
    display: flex;
    justify-content: center;
    margin-top: 12px;
  }
  .specialties__list li {
    font-size: 22px;
    color: var(--service);
    padding: 3px 17px;
    line-height: 30px;
  }
  .specialties__list li + li { border-left: 2px solid var(--rule); }

  .droplets {
    position: absolute;
    left: 108px;
    top: 228px;
    width: 442px;
    height: 86px;
    border-radius: 40px;
    background: radial-gradient(ellipse at 50% 50%, rgba(127,179,227,0.75) 0%, rgba(127,179,227,0.25) 55%, rgba(127,179,227,0) 80%);
  }
</style>
</head>
<body>
  <section class="card card--front">
    <div class="water-drop" role="img" aria-label="Illustration of a falling water drop"></div>
    <div class="brand">
      <span class="brand__name"><span class="brand__mark"></span>KESTERLY PLUMBING</span>
      <span class="brand__trade">&amp; Gasfitting</span>
    </div>
    <div class="holder">
      <p class="holder__name">Marcus Kesterly</p>
      <p class="holder__licence">License no. - 73804</p>
    </div>
    <div class="contact">
      <p class="contact__email">m_kesterly@mailnest.com.au</p>
      <p class="contact__phone">
        <svg viewBox="0 0 14 20" aria-hidden="true"><rect x="1" y="1" width="12" height="18" rx="2" fill="none" stroke="#2b2b2e" stroke-width="2"/><rect x="3" y="3.5" width="8" height="11" fill="#2b2b2e"/></svg>
        049-361-2085
      </p>
    </div>
  </section>

  <section class="card card--back">
    <div class="brand">
      <span class="brand__name"><span class="brand__mark"></span>KESTERLY PLUMBING</span>
      <span class="brand__trade">&amp; Gasfitting</span>
    </div>
    <div class="specialties">
      <p class="specialties__title">Specialising in:</p>
      <ul class="specialties__list">
        <li>new homes</li>
        <li>maintenance</li>
        <li>renovations</li>
      </ul>
    </div>
    <div class="droplets" role="img" aria-label="Scattered water droplets illustration"></div>
  </section>
</body>
</html>
```